KELVOR EHS & S Resources

We would like Markvelo to update and make our environmental, health and safety resources business website more professional and using our new logo and color scheme.
https://kelvorehsresources.com/

```html
<!DOCTYPE html>
<html lang="en">
<head>
<meta charset="utf-8">
<title>KELVOR EHS &amp; S Resources</title>
<link href="https://fonts.googleapis.com/css2?family=Poppins:wght@300;400;500;600;700&display=swap" rel="stylesheet">
<style>
:root{
  --ink:#1a1d24;
  --text:#5b616e;
  --muted:#8a909c;
  --blue:#1f7fe0;
  --lime:#c9d82b;
  --dark:#141820;
  --line:#e3e6ec;
  --soft:#f5f7fa;
  --white:#ffffff;
}
*{box-sizing:border-box;margin:0;padding:0}
html,body{width:1200px;height:3312px;overflow:hidden}
body{font-family:"Poppins",sans-serif;color:var(--text);background:var(--white);position:relative}
a{color:inherit;text-decoration:none}
.brand{display:flex;align-items:center;gap:10px;font-weight:700;font-size:20px;color:var(--ink);letter-spacing:.5px}
.brand-dot{width:22px;height:22px;border-radius:50%;background:var(--blue)}
.site-header{position:absolute;top:0;left:0;width:1200px;height:84px;background:var(--white);display:flex;align-items:center;justify-content:space-between;padding:0 70px;z-index:2}
.main-nav{display:flex;align-items:center;gap:34px;font-size:14px;color:var(--ink);font-weight:500}
.btn{display:inline-block;background:var(--blue);color:var(--white);font-weight:500;font-size:14px;padding:11px 24px;border-radius:4px}
.hero{position:absolute;top:84px;left:0;width:1200px;height:456px;background:linear-gradient(110deg,#11151c 0%,#2b3038 45%,#7d7b70 80%,#a7a190 100%)}
.hero-copy{position:absolute;left:100px;top:100px;color:var(--white)}
.hero-kicker{font-size:14px;font-weight:500;color:#d7dbe2;margin-bottom:8px}
.hero-title{font-size:46px;font-weight:700;line-height:1.12;max-width:600px}
.hero-title span{color:var(--lime)}
.hero-bar{position:absolute;left:100px;top:300px;display:flex;gap:14px}
.hero-bar .btn{padding:13px 28px}
.btn-ghost{border:1px solid rgba(255,255,255,.6);color:var(--white);padding:13px 28px;border-radius:4px;font-size:14px}
.section-label{font-size:13px;font-weight:600;color:var(--blue);letter-spacing:1px;text-transform:uppercase;margin-bottom:10px}
.section-title{font-size:38px;font-weight:600;color:var(--ink);line-height:1.2}
.about{position:absolute;top:620px;left:0;width:1200px;height:560px}
.about-photo{position:absolute;left:330px;top:90px;width:380px;height:420px;border-radius:6px;background:linear-gradient(135deg,#d9d4a8,#9d9a6c)}
.about-badge{position:absolute;left:640px;top:110px;width:130px;height:90px;background:var(--white);border-radius:6px;box-shadow:0 8px 24px rgba(0,0,0,.12);display:flex;flex-direction:column;justify-content:center;align-items:center;font-size:12px;color:var(--ink);text-align:center}
.about-badge b{font-size:26px;color:var(--blue)}
.about-copy{position:absolute;left:800px;top:90px;width:360px}
.about-copy .section-title{font-size:30px}
.about-copy p{font-size:14px;line-height:1.75;margin:18px 0 22px}
.more{font-size:14px;font-weight:600;color:var(--blue)}
.services{position:absolute;top:1240px;left:0;width:1200px;height:600px}
.services-head{position:absolute;left:70px;top:130px;width:460px}
.card{background:var(--white);border:1px solid var(--line);border-radius:8px;padding:26px 24px;overflow:hidden}
.card h3{font-size:17px;font-weight:600;color:var(--ink);margin:14px 0 8px}
.card p{font-size:13px;line-height:1.6}
.icon{width:44px;height:44px;border-radius:8px;background:#eaf3fd;display:flex;align-items:center;justify-content:center}
.svc-top{position:absolute;left:560px;top:80px;display:flex;gap:24px}
.svc-top .card{width:290px;height:210px}
.svc-row{position:absolute;left:70px;top:320px;display:flex;gap:24px}
.svc-row .card{width:255px;height:210px}
.testimonials{position:absolute;top:1880px;left:0;width:1200px;height:520px;background:var(--soft)}
.test-head{text-align:center;padding-top:80px}
.test-head .section-title{max-width:640px;margin:0 auto}
.test-grid{position:absolute;left:36px;top:260px;display:flex;gap:24px}
.test-grid .card{width:264px;height:220px;display:flex;flex-direction:column;justify-content:space-between}
.person{display:flex;align-items:center;gap:12px}
.avatar{width:42px;height:42px;border-radius:50%;background:#cfd6e0}
.person b{display:block;font-size:14px;color:var(--ink);font-weight:600}
.person span{font-size:12px;color:var(--muted)}
.contact{position:absolute;top:2420px;left:0;width:1200px;height:500px}
.contact-photo{position:absolute;left:0;top:0;width:780px;height:500px;background:linear-gradient(120deg,#9b4fd6 0%,#c9c98a 30%,#d8d49b 70%,#ece9cf 100%)}
.contact-form{position:absolute;left:850px;top:90px;width:300px}
.contact-form .section-title{font-size:32px}
.field{font-size:13px;color:var(--muted);border-bottom:1px solid var(--line);padding:12px 0;margin-top:6px}
.field-pair{display:flex;gap:20px}
.field-pair .field{flex:1}
.field-message{height:80px}
.contact-form .btn{margin-top:26px}
.site-footer{position:absolute;top:2960px;left:0;width:1200px;height:352px;background:var(--white);border-top:1px solid var(--line)}
.foot-brand{position:absolute;left:290px;top:60px;width:300px}
.foot-brand p{font-size:13px;line-height:1.7;margin:16px 0}
.socials{display:flex;gap:10px}
.socials i{width:26px;height:26px;border-radius:50%;background:var(--ink);display:block}
.foot-col{position:absolute;top:60px}
.foot-col h4{font-size:16px;color:var(--ink);font-weight:600;margin-bottom:16px}
.foot-col li{list-style:none;font-size:13px;margin-bottom:10px}
.foot-links{left:650px}
.foot-services{left:800px}
.foot-contact{left:1010px}
.foot-bottom{position:absolute;left:0;bottom:0;width:1200px;height:56px;border-top:1px solid var(--line);display:flex;align-items:center;justify-content:space-between;padding:0 70px;font-size:12px}
</style>
</head>
<body>

<header class="site-header">
  <div class="brand"><i class="brand-dot"></i>KELVOR</div>
  <nav class="main-nav">
    <a href="#">Home</a><a href="#">About Us</a><a href="#">Services</a><a href="#">Security</a>
    <a class="btn" href="#">Contact Us</a>
  </nav>
</header>

<section class="hero" role="img" aria-label="Photo of a safety worker in protective gear on an industrial site">
  <div class="hero-copy">
    <p class="hero-kicker">We Lead in EHS &amp; Security Resources</p>
    <h1 class="hero-title">Experience Reputation. <span>Respect. Results</span></h1>
  </div>
  <div class="hero-bar">
    <a class="btn" href="#">Get Started</a>
    <a class="btn-ghost" href="#">Our Services</a>
  </div>
</section>

<section class="about">
  <div class="about-photo" role="img" aria-label="Photo of an EHS specialist inspecting a facility"></div>
  <div class="about-badge"><b>40</b>years of experience</div>
  <div class="about-copy">
    <p class="section-label">About Us</p>
    <h2 class="section-title">We have Education, Experience &amp; Credentials you can Trust</h2>
    <p>Our principal has over forty years of experience in the environmental, health, safety and security field, serving clients in manufacturing, healthcare, education, industrial, commercial and government sectors.</p>
    <a class="more" href="#">Learn more →</a>
  </div>
</section>

<section class="services">
  <div class="services-head">
    <p class="section-label">Services</p>
    <h2 class="section-title">Environmental, health and safety services</h2>
  </div>
  <div class="svc-top">
    <div class="card"><div class="icon"><svg width="22" height="22" viewBox="0 0 24 24" fill="none" stroke="#1f7fe0" stroke-width="2"><circle cx="11" cy="11" r="7"/><path d="M16 16l5 5"/></svg></div><h3>EHS Consulting</h3><p>Compliance with OSHA and EPA regulations, audits and written programs.</p></div>
    <div class="card"><div class="icon"><svg width="22" height="22" viewBox="0 0 24 24" fill="none" stroke="#1f7fe0" stroke-width="2"><path d="M12 3l8 4v5c0 5-4 8-8 9-4-1-8-4-8-9V7z"/></svg></div><h3>Security</h3><p>Site security assessments, planning and response for your team.</p></div>
  </div>
  <div class="svc-row">
    <div class="card"><div class="icon"><svg width="22" height="22" viewBox="0 0 24 24" fill="none" stroke="#1f7fe0" stroke-width="2"><path d="M3 8l9-4 9 4-9 4z"/><path d="M7 10v5c3 2 7 2 10 0v-5"/></svg></div><h3>Training</h3><p>Hands-on safety training tailored to your workforce and needs.</p></div>
    <div class="card"><div class="icon"><svg width="22" height="22" viewBox="0 0 24 24" fill="none" stroke="#1f7fe0" stroke-width="2"><path d="M12 20s-7-4-7-10a4 4 0 0 1 7-2 4 4 0 0 1 7 2c0 6-7 10-7 10z"/></svg></div><h3>Occupational Health</h3><p>Exposure monitoring and health programs for safer workplaces.</p></div>
    <div class="card"><div class="icon"><svg width="22" height="22" viewBox="0 0 24 24" fill="none" stroke="#1f7fe0" stroke-width="2"><path d="M3 9h12a3 3 0 1 0-3-3"/><path d="M3 15h15a3 3 0 1 1-3 3"/></svg></div><h3>Indoor Air Environment</h3><p>Indoor air quality testing, mold review and clear reporting.</p></div>
    <div class="card"><div class="icon"><svg width="22" height="22" viewBox="0 0 24 24" fill="none" stroke="#1f7fe0" stroke-width="2"><rect x="4" y="4" width="16" height="16" rx="2"/><path d="M8 12l3 3 5-6"/></svg></div><h3>Management</h3><p>Environmental management systems built to fit your operation.</p></div>
  </div>
</section>

<section class="testimonials">
  <div class="test-head">
    <p class="section-label">Testimonials</p>
    <h2 class="section-title">We Provide Services for a Huge Number of Customers</h2>
  </div>
  <div class="test-grid">
    <div class="card"><p>Kelvor helped us build a safety program that our whole plant understands. Audits are now smooth and our team feels confident.</p><div class="person"><i class="avatar"></i><div><b>Dana Whitlock</b><span>Plant Director</span></div></div></div>
    <div class="card"><p>Clear advice, fast answers and real expertise. Their training sessions were practical and our staff actually enjoyed them.</p><div class="person"><i class="avatar"></i><div><b>Marcus Fenley</b><span>HR Director</span></div></div></div>
    <div class="card"><p>The indoor air review was thorough and the report was easy to act on. We would gladly work with them again.</p><div class="person"><i class="avatar"></i><div><b>Elena Brandt</b><span>Facility Lead</span></div></div></div>
    <div class="card"><p>Professional, responsive and honest. They know the rules well and explain them in plain, useful terms.</p><div class="person"><i class="avatar"></i><div><b>Owen Carrick</b><span>Operations Head</span></div></div></div>
  </div>
</section>

<section class="contact">
  <div class="contact-photo" role="img" aria-label="Photo of an industrial work site with safety equipment"></div>
  <form class="contact-form">
    <p class="section-label">Contact Us</p>
    <h2 class="section-title">Get in Touch</h2>
    <div class="field-pair"><div class="field">Name</div><div class="field">Email</div></div>
    <div class="field">Phone</div>
    <div class="field field-message">Message</div>
    <a class="btn" href="#">Submit</a>
  </form>
</section>

<footer class="site-footer">
  <div class="foot-brand">
    <div class="brand"><i class="brand-dot"></i>KELVOR</div>
    <p>Environmental, health, safety and security resources for organizations that value their people.</p>
    <div class="socials"><i></i><i></i><i></i><i></i></div>
  </div>
  <div class="foot-col foot-links"><h4>Links</h4><ul><li>Home</li><li>About Us</li><li>Services</li><li>Pages</li></ul></div>
  <div class="foot-col foot-services"><h4>Services</h4><ul><li>EHS Consulting</li><li>Security</li><li>Training</li><li>Occupational Health</li><li>Indoor Air Environment</li></ul></div>
  <div class="foot-col foot-contact"><h4>Contact Info</h4><ul><li>(555) 014-2290</li><li>info@kelvorehs.com</li><li>kelvorehsresources.com</li></ul></div>
  <div class="foot-bottom"><span>© 2024 KELVOR EHS &amp; S Resources. All rights reserved.</span><span>Privacy Policy · Terms</span></div>
</footer>

</body>
</html>
```